K9 Orbit needs a business card designed

We need a business card designed for K9 Orbit, an expansion of K9 Systems Pty Ltd (www.k9systems.com.au)

We provide high quality professional services for the Australian space industry. Our clients include the Southern Launch Bureau and companies working in the space industry. We identify people with space related skills both locally and internationally who are then contracted by clients to create products and support space launch activities.

Colours to be used:
- Navy blue #000080
- Rocket metallic #8A7F8D
- Platinum #E5E4E2
- Black #000000
- White #FFFFFF

*Front of the card*
I have attached our K9 Orbit logo, which needs to be the main item on the card. The 'Space' text should be placed to the right of the 'K9' part rather than below, similar to the attached K9 Systems card, which this card should match.

If subtext is included, however, it should read ‘Labour Hire • Consultancy • Project Delivery’ rather than the ‘Design • Build • Test • Maintain’ of the K9 Systems card.

A black background (rather than blue background in the K9 Systems card) might be good, with a white pattern as in the K9 Systems card. If colour is used, the logo should be in its standard colours (as provided for the K9 Orbit logo).

*Back of the card*
Include a smaller K9 Orbit logo on the back.

We need the following details for K9 Orbit personnel (as a template for entry):
- Name
- Company Position
- Mobile Number
- Email
- Office Address
- Include the K9 Orbit website: www.k9orbit.com.au

Overall, we'd like to see a design that communicates the adventure of space, professional integrity, and customer service. We look forward to seeing what you can come up with.

Target Market(s)

We provide high quality professional services for the Australian space industry. Our clients include the Southern Launch Bureau and companies working in the space industry.

Contact Information for Business Card

- Name
- Company Position
- Mobile Number
- Email
- Office Address

Requirements
Must have
• See project description.

```html
<!DOCTYPE html>
<html lang="en">
<head>
<meta charset="utf-8">
<title>K9 Orbit business card</title>
<link href="https://fonts.googleapis.com/css2?family=Montserrat:wght@400;500;600&family=Lato:wght@400;700&display=swap" rel="stylesheet">
<style>
  :root {
    --navy: #1b1960;
    --navy-deep: #141248;
    --navy-faint: #232270;
    --metal: #8a7f8d;
    --white: #ffffff;
    --backdrop: #1c1c1e;
  }
  * { box-sizing: border-box; margin: 0; padding: 0; }
  html, body { width: 1200px; height: 900px; overflow: hidden; background: var(--backdrop); }
  .card {
    position: absolute; width: 700px; height: 400px; border-radius: 26px; overflow: hidden;
    background: linear-gradient(135deg, var(--navy) 0%, var(--navy-deep) 100%);
    color: var(--white); box-shadow: 0 18px 40px rgba(0,0,0,.55);
  }
  .card-front { left: 60px; top: 40px; }
  .card-back { left: 440px; top: 470px; }

  .front-watermark {
    position: absolute; left: 150px; top: 20px;
    font-family: "Montserrat", sans-serif; font-weight: 600; font-size: 330px; line-height: 1;
    color: var(--navy-faint); letter-spacing: -10px;
  }
  .front-lockup { position: absolute; left: 170px; top: 150px; display: flex; align-items: center; gap: 26px; }
  .brand-mark {
    font-family: "Montserrat", sans-serif; font-weight: 600; font-size: 60px; line-height: 1; color: var(--white);
  }
  .brand-word {
    font-family: "Montserrat", sans-serif; font-weight: 500; font-size: 62px; letter-spacing: 26px; line-height: 1;
  }
  .front-services {
    position: absolute; left: 0; right: 0; bottom: 48px; text-align: center;
    font-family: "Montserrat", sans-serif; font-size: 17px; letter-spacing: 1px;
  }

  .back-panel { position: absolute; inset: 0; }
  .back-mark {
    position: absolute; right: 70px; top: 95px;
    font-family: "Montserrat", sans-serif; font-weight: 600; font-size: 120px; line-height: 1; color: var(--navy);
  }
  .back-info { position: absolute; left: 44px; top: 40px; width: 360px; }
  .back-word { font-family: "Montserrat", sans-serif; font-weight: 500; font-size: 44px; letter-spacing: 20px; line-height: 1; }
  .back-services { font-family: "Montserrat", sans-serif; font-size: 9.5px; margin-top: 8px; letter-spacing: .3px; }
  .person-name { font-family: "Montserrat", sans-serif; font-weight: 600; font-size: 24px; margin-top: 34px; letter-spacing: .5px; }
  .person-role { font-family: "Lato", sans-serif; font-size: 17px; margin-top: 2px; }
  .office-address { font-family: "Lato", sans-serif; font-size: 16px; line-height: 1.3; margin-top: 22px; }
  .contact-list { list-style: none; margin-top: 18px; font-family: "Lato", sans-serif; font-size: 16px; line-height: 1.5; }
  .contact-list li { display: flex; align-items: center; gap: 10px; }
  .contact-list svg { width: 13px; height: 13px; fill: var(--white); flex: none; }
</style>
</head>
<body>
  <section class="card card-front">
    <div class="front-watermark" aria-hidden="true">K9</div>
    <div class="front-lockup">
      <span class="brand-mark">K9</span>
      <span class="brand-word">ORBIT</span>
    </div>
    <p class="front-services">Consultancy • Command • Control • Communications • Labour Hire</p>
  </section>

  <section class="card card-back">
    <svg class="back-panel" viewBox="0 0 700 400" preserveAspectRatio="none" aria-hidden="true">
      <path d="M330 0 C 330 170 420 320 600 400 L700 400 L700 0 Z" fill="var(--metal)"/>
      <path d="M358 0 C 355 170 450 320 640 400 L700 400 L700 0 Z" fill="var(--white)"/>
    </svg>
    <div class="back-mark">K9</div>
    <div class="back-info">
      <div class="back-word">ORBIT</div>
      <p class="back-services">Consultancy • Control • Communications • Labour Hire</p>
      <p class="person-name">AARON VELDE</p>
      <p class="person-role">Co-Founder</p>
      <p class="office-address">Level 4, 18 Halifax Lane<br>Adelaide SA 5000</p>
      <ul class="contact-list">
        <li><svg viewBox="0 0 24 24"><path d="M6.6 10.8a15 15 0 0 0 6.6 6.6l2.2-2.2c.3-.3.7-.4 1-.2 1.1.4 2.3.6 3.6.6.6 0 1 .4 1 1V20c0 .6-.4 1-1 1A17 17 0 0 1 3 4c0-.6.4-1 1-1h3.5c.6 0 1 .4 1 1 0 1.3.2 2.5.6 3.6.1.3 0 .7-.2 1z"/></svg>(08) 7100 4821</li>
        <li><svg viewBox="0 0 24 24"><path d="M2 5h20v14H2z M2 5l10 8 10-8" fill="none" stroke="#fff" stroke-width="2"/></svg>aaron@k9orbit.com.au</li>
        <li><svg viewBox="0 0 24 24"><circle cx="12" cy="12" r="9" fill="none" stroke="#fff" stroke-width="2"/><path d="M3 12h18M12 3c3 3 3 15 0 18M12 3c-3 3-3 15 0 18" fill="none" stroke="#fff" stroke-width="1.6"/></svg>www.k9orbit.com.au</li>
      </ul>
    </div>
  </section>
</body>
</html>
```